Pruett Family Motto/Mission Statement

We are creating a poster to be hung in our home with several purpose statements for our family (last name Pruett, and "The Pruett Family" should be included in the poster prominently). The text that we want included is in the attached file.

Our kids range in age from 8 to 17, so we are looking for something that is homey and cheerful, but fairly bold and oriented to older kids (and not so much younger kids).

I've attached a couple of example poster/statements that we generally like. Overall color scheme could include blues and greens and possibly some brown.

Anticipated size of this poster would be 18"x24" with a portrait orientation.

```html
<!DOCTYPE html>
<html lang="en">
<head>
<meta charset="utf-8">
<title>The Pruett Family – Family Mission Statement</title>
<link rel="stylesheet" href="https://fonts.googleapis.com/css2?family=Oswald:wght@500;700&family=Lobster&family=Lobster+Two:ital,wght@1,700&family=Questrial&family=Black+Ops+One&family=Archivo+Black&family=Fjord+One&family=Bebas+Neue&display=swap">
<style>
  :root {
    --paper-light: #f1ecdf;
    --paper-mid: #e6dfcd;
    --paper-dark: #cfc5ad;
    --slate-blue: #36556a;
    --ink: #121212;
  }
  html, body {
    margin: 0;
    padding: 0;
    width: 900px;
    height: 1200px;
    overflow: hidden;
    background: var(--paper-mid);
  }
  .poster {
    position: relative;
    width: 900px;
    height: 1200px;
    background:
      radial-gradient(ellipse at 50% 45%, var(--paper-light) 0%, var(--paper-mid) 65%, var(--paper-dark) 100%);
  }
  .poster svg { display: block; }
  .title { font-family: "Oswald", sans-serif; font-weight: 700; }
  .title-shade { fill: var(--slate-blue); }
  .title-face { fill: var(--slate-blue); stroke: var(--paper-light); stroke-width: 3; paint-order: stroke; }
  .script { font-family: "Lobster Two", cursive; font-style: italic; font-weight: 700; fill: var(--ink); }
  .script-accent { font-family: "Lobster", cursive; font-style: normal; font-weight: 400; }
  .gothic { font-family: "Questrial", sans-serif; fill: var(--slate-blue); }
  .stencil { font-family: "Black Ops One", sans-serif; fill: var(--ink); }
  .heavy { font-family: "Archivo Black", sans-serif; fill: var(--slate-blue); }
  .wide-serif { font-family: "Fjord One", serif; fill: var(--ink); font-weight: 700; }
  .condensed { font-family: "Oswald", sans-serif; font-weight: 500; fill: var(--slate-blue); }
  .poster-caps { font-family: "Bebas Neue", sans-serif; fill: var(--ink); }
</style>
</head>
<body>
<main class="poster">
  <svg width="900" height="1200" viewBox="0 0 900 1200" role="img" aria-label="The Pruett Family mission statement">
    <g class="family-name">
      <text class="title title-shade" x="45" y="208" font-size="122" textLength="825" lengthAdjust="spacingAndGlyphs">THE PRUETT FAMILY</text>
      <text class="title title-face" x="40" y="203" font-size="122" textLength="825" lengthAdjust="spacingAndGlyphs">THE PRUETT FAMILY</text>
    </g>

    <text class="script" x="42" y="288" font-size="62" textLength="813" lengthAdjust="spacingAndGlyphs">We love to <tspan class="script-accent">learn</tspan> new things.</text>

    <text class="gothic" x="193" y="368" font-size="58" textLength="497" lengthAdjust="spacingAndGlyphs">WE LOOK AT LIFE</text>
    <text class="gothic" x="42" y="443" font-size="58" textLength="818" lengthAdjust="spacingAndGlyphs">THROUGH A POSITIVE LENS.</text>

    <text class="stencil" x="45" y="515" font-size="28" textLength="812" lengthAdjust="spacingAndGlyphs"><tspan font-size="36">KINDNESS</tspan> GUIDES OUR WORDS AND DEEDS.</text>

    <text class="heavy" x="128" y="588" font-size="52" textLength="634" lengthAdjust="spacingAndGlyphs">We create adventure and</text>
    <text class="heavy" x="40" y="660" font-size="52" textLength="820" lengthAdjust="spacingAndGlyphs">choose experiences over things.</text>

    <text class="wide-serif" x="50" y="738" font-size="52" textLength="798" lengthAdjust="spacingAndGlyphs">We commit to be fit.</text>

    <text class="condensed" x="47" y="822" font-size="66" textLength="785" lengthAdjust="spacingAndGlyphs">OUR DAYS ARE BRIGHTENED BY</text>
    <text class="condensed" x="147" y="900" font-size="66" textLength="608" lengthAdjust="spacingAndGlyphs">A SENSE OF HUMOR.</text>

    <text class="poster-caps" x="160" y="985" font-size="82" textLength="562" lengthAdjust="spacingAndGlyphs">WE DO WHAT IS RIGHT</text>
    <text class="poster-caps" x="70" y="1093" font-size="66" textLength="760" lengthAdjust="spacingAndGlyphs">EVEN WHEN NO ONE IS WATCHING.</text>
  </svg>
</main>
</body>
</html>
```